Velmira Body Oil Label for 4 -8 oz bottles

We are selling 4 and 8 oz body oils and need a label to put on our bottles. I'm not sure if we want a label for the front and also the back of the bottle or just one label in the front. You can give me examples of each way. Attached is our logo on a blue background but the background will change colors depending on the scent as specified in the design description. Our bottle will be either clear or white with a pump spray type lid as shown in the attached example. Attached are also our design criteria which is needed for the labels.
Updates

We have decided to use the disc top cap and not the pump spray cap. If you are able to, please show us the design on the 4 oz bottle with the disc top cap. Thanks

Target Market(s)

women

Industry/Entity Type

skincare, cosmetics

Font styles to use
Serif
Sans Serif

Requirements
Must have
• stylish name for each scented oil which contrasts the font in the logo. Also must have darker colors since the logo colors are lighter.
Nice to have
• Border around the labels, maybe one solid color or maybe two complimenting colors which go well with the fragrnace name
Should not have
• background colors that match the logo colors

```html
<!DOCTYPE html>
<html lang="en">
<head>
<meta charset="UTF-8">
<title>Velmira Body Oils – Soft Lavender Label</title>
<link href="https://fonts.googleapis.com/css2?family=Caveat+Brush&family=Roboto:ital,wght@0,400;0,500;0,700;1,400;1,500;1,700&display=swap" rel="stylesheet">
<style>
  :root {
    --canvas-bg: #3a3a3c;
    --label-purple: #562a84;
    --label-lilac: #d2bbdd;
    --ink-purple: #5a2d8c;
    --ink-dark: #3b2a44;
    --pale-lilac: #d9c5e6;
    --white: #ffffff;
  }
  * { margin: 0; padding: 0; box-sizing: border-box; }
  html, body {
    width: 1200px; height: 900px; overflow: hidden;
    background: var(--canvas-bg);
    font-family: "Roboto", Arial, sans-serif;
  }
  .canvas { position: relative; width: 1200px; height: 900px; }

  .side-title {
    position: absolute; top: 128px; width: 227px; text-align: center;
    font-family: "Roboto", Arial, sans-serif; font-style: italic; font-weight: 500;
    font-size: 31px; color: var(--pale-lilac);
  }
  .side-title--front { left: 111px; }
  .side-title--back { left: 362px; }

  .label {
    position: absolute; top: 188px; width: 227px; height: 527px;
    border-radius: 20px; overflow: hidden; background: var(--label-lilac);
    text-align: center;
  }
  .label--front { left: 111px; }
  .label--back { left: 362px; }

  .front-panel {
    position: absolute; left: 0; top: 0; width: 100%; height: 333px;
    background: var(--label-purple);
  }
  .brand {
    position: absolute; top: 62px; left: 0; width: 100%;
    display: flex; align-items: center; justify-content: center; gap: 8px;
  }
  .brand-dot { width: 10px; height: 10px; border-radius: 50%; background: var(--white); }
  .brand-name { font-family: "Roboto", Arial, sans-serif; font-weight: 400; font-size: 30px; color: var(--white); letter-spacing: 0.5px; }

  .scent-name {
    font-family: "Caveat Brush", cursive; font-weight: 400; letter-spacing: 0.5px;
  }
  .front-panel .scent-name {
    position: absolute; top: 212px; left: 0; width: 100%;
    font-size: 32px; color: var(--pale-lilac);
  }
  .rule { position: absolute; left: 68px; width: 92px; height: 1.5px; }
  .rule--light { top: 267px; background: var(--pale-lilac); }
  .rule--dark { top: 389px; background: var(--ink-purple); }

  .claims {
    position: absolute; top: 403px; left: 0; width: 100%;
    font-style: italic; font-size: 10px; line-height: 13px; color: var(--ink-purple);
  }
  .net-weight {
    position: absolute; top: 492px; left: 0; width: 100%;
    font-weight: 500; font-size: 10.5px; color: var(--ink-purple);
  }

  .label--back .scent-name {
    position: absolute; top: 26px; left: 0; width: 100%;
    font-size: 33px; color: var(--ink-purple);
  }
  .info-block { position: absolute; left: 18px; width: 191px; }
  .info-heading {
    font-style: italic; font-weight: 700; font-size: 10.5px; color: var(--ink-purple);
    margin-bottom: 8px;
  }
  .info-text { font-size: 8.6px; line-height: 11.3px; color: var(--ink-dark); }
  .info--ingredients { top: 80px; }
  .info--directions { top: 179px; }
  .info--warnings { top: 231px; }
  .info--distributor { top: 446px; }
</style>
</head>
<body>
<main class="canvas">
  <h2 class="side-title side-title--front">front</h2>
  <h2 class="side-title side-title--back">back</h2>

  <section class="label label--front" aria-label="Front label">
    <div class="front-panel">
      <div class="brand">
        <span class="brand-dot"></span>
        <span class="brand-name">Velmira</span>
      </div>
      <h1 class="scent-name">Soft Lavender</h1>
      <div class="rule rule--light"></div>
    </div>
    <div class="rule rule--dark"></div>
    <p class="claims">Non-Greasy<br>With Vitamin E<br>Ultra Moisturizing</p>
    <p class="net-weight">Net Wt. 4 fl. oz. (118 mL)</p>
  </section>

  <section class="label label--back" aria-label="Back label">
    <h1 class="scent-name">Soft Lavender</h1>

    <div class="info-block info--ingredients">
      <h3 class="info-heading">Ingredients :</h3>
      <p class="info-text">Cocos Nucifera (Coconut) Oil, Prunus Amygdalus Dulcis (Almond) Oil, Vitis Vinifera (Grapeseed) Oil, Sesamum Indicum (Sesame) Seed Oil, Simmondsia Chinensis (Jojoba) Oil, Tocopheryl Acetate (Vitamin E). Essential oils, and fragrances.</p>
    </div>

    <div class="info-block info--directions">
      <h3 class="info-heading">Directions :</h3>
      <p class="info-text">Apply a small amount to skin and massage until absorbed. Use daily for best results.</p>
    </div>

    <div class="info-block info--warnings">
      <h3 class="info-heading">Warnings :</h3>
      <p class="info-text">For external use only.<br>Avoid contact with eyes.<br>Discontinue use if irritation occurs.<br>Keep out of reach of children.<br>Contains nut oils — use with caution if you have nut allergies.</p>
    </div>

    <div class="info-block info--distributor">
      <h3 class="info-heading">Distributed by</h3>
      <p class="info-text">Velmira<br>2217 Larkspur Lane<br>Fort Collins, CO 80525<br>Made in USA</p>
    </div>
  </section>
</main>
</body>
</html>
```